Design Cloud for Core Values & Attributes

See Image Example Below "Word Cloud" this is what we would like this to look like.
The second image is all of the Core Value and Attributes I will list below.
CORE VALUES need to be the bigger words (based off the image I sent) Capitalized, BOLD, Navy
Independence, Capitalism, Trust, Fun, Safety, Growth
ATTRIBUTES need to be the smaller words, lower case, non-bold, lighter blue mixed in (based off the image I sent):
Humility, Consistency, Open Mindedness, Curiosity, Selflessness, Caring, Conscientiousness, Honorable, Cunning, Competitive, Compartmentalization, Innovative, Perseverance, Authenticity, Decisiveness, Self-efficacy, Accountability, Generosity, Humor, Optimism, Resilience, Inclusive, Insouciance to what others think, Courage, Decisive, Curious, Integrity

```html
<!DOCTYPE html>
<html lang="en">
<head>
<meta charset="utf-8">
<title>Core Values Word Cloud</title>
<link rel="stylesheet" href="https://fonts.googleapis.com/css2?family=Bebas+Neue&family=Roboto+Condensed:wght@300&display=swap">
<style>
  :root {
    --navy: #062470;
    --value-blue: #0677ba;
    --attr-dark: #0b5c96;
    --attr-mid: #2f8ed6;
    --attr-light: #7fa6cf;
    --paper: #ffffff;
  }
  html, body {
    margin: 0;
    padding: 0;
    width: 1200px;
    height: 1200px;
    overflow: hidden;
    background: var(--paper);
  }
  .word-cloud {
    display: block;
    width: 1200px;
    height: 1200px;
  }
  .core-value {
    font-family: 'Bebas Neue', 'Oswald', sans-serif;
    font-weight: 400;
  }
  .core-value--navy { fill: var(--navy); }
  .core-value--blue { fill: var(--value-blue); }
  .attribute {
    font-family: 'Roboto Condensed', 'Arial Narrow', sans-serif;
    font-weight: 300;
    font-size: 50px;
  }
  .attribute--dark { fill: var(--attr-dark); }
  .attribute--mid { fill: var(--attr-mid); }
  .attribute--light { fill: var(--attr-light); }
</style>
</head>
<body>
<svg class="word-cloud" viewBox="0 0 1200 1200" xmlns="http://www.w3.org/2000/svg" role="img" aria-label="Core values and attributes word cloud">
  <rect width="1200" height="1200" fill="var(--paper)"/>
  <g transform="translate(0 175) scale(0.688) translate(-95 -351)">

    <!-- Core values -->
    <text class="core-value core-value--navy" x="408" y="1018" font-size="283" textLength="420" lengthAdjust="spacingAndGlyphs">CORE</text>
    <text class="core-value core-value--navy" x="640" y="1262" font-size="286" textLength="628" lengthAdjust="spacingAndGlyphs">VALUES</text>
    <text class="core-value core-value--blue" x="852" y="1027" font-size="170" textLength="765" lengthAdjust="spacingAndGlyphs">INDEPENDENCE</text>
    <text class="core-value core-value--blue" x="1296" y="1182" font-size="171" textLength="319" lengthAdjust="spacingAndGlyphs">TRUST</text>
    <text class="core-value core-value--blue" x="422" y="1172" font-size="171" textLength="189" lengthAdjust="spacingAndGlyphs">FUN</text>
    <text class="core-value core-value--blue" x="527" y="806" font-size="171" textLength="379" lengthAdjust="spacingAndGlyphs">SAFETY</text>
    <text class="core-value core-value--blue" x="580" y="1420" font-size="171" textLength="423" lengthAdjust="spacingAndGlyphs">GROWTH</text>
    <text class="core-value core-value--blue" transform="translate(394 1235) rotate(-90)" font-size="174" textLength="597" lengthAdjust="spacingAndGlyphs">CAPITALISM</text>

    <!-- Attributes -->
    <text class="attribute attribute--light" x="542" y="618" textLength="192" lengthAdjust="spacingAndGlyphs">honorable</text>
    <text class="attribute attribute--dark" x="765" y="613" textLength="155" lengthAdjust="spacingAndGlyphs">integrity</text>
    <text class="attribute attribute--light" x="542" y="675" textLength="118" lengthAdjust="spacingAndGlyphs">caring</text>
    <text class="attribute attribute--mid" x="691" y="672" textLength="224" lengthAdjust="spacingAndGlyphs">authenticity</text>
    <text class="attribute attribute--light" x="907" y="763" textLength="155" lengthAdjust="spacingAndGlyphs">decisive</text>
    <text class="attribute attribute--light" x="902" y="822" textLength="163" lengthAdjust="spacingAndGlyphs">curiosity</text>
    <text class="attribute attribute--mid" x="833" y="877" textLength="232" lengthAdjust="spacingAndGlyphs">self-efficacy</text>
    <text class="attribute attribute--dark" x="1133" y="753" textLength="142" lengthAdjust="spacingAndGlyphs">curious</text>
    <text class="attribute attribute--light" x="1129" y="810" textLength="180" lengthAdjust="spacingAndGlyphs">optimism</text>
    <text class="attribute attribute--light" x="1128" y="867" textLength="224" lengthAdjust="spacingAndGlyphs">competitive</text>
    <text class="attribute attribute--mid" x="1385" y="866" textLength="200" lengthAdjust="spacingAndGlyphs">generosity</text>
    <text class="attribute attribute--light" x="465" y="1216" textLength="150" lengthAdjust="spacingAndGlyphs">humility</text>
    <text class="attribute attribute--mid" x="386" y="1285" textLength="229" lengthAdjust="spacingAndGlyphs">consistency</text>
    <text class="attribute attribute--light" x="313" y="1342" textLength="256" lengthAdjust="spacingAndGlyphs">perseverance</text>
    <text class="attribute attribute--dark" x="444" y="1410" textLength="123" lengthAdjust="spacingAndGlyphs">humor</text>
    <text class="attribute attribute--mid" x="378" y="1470" textLength="624" lengthAdjust="spacingAndGlyphs">insouciance to what others think</text>
    <text class="attribute attribute--light" x="1284" y="1245" textLength="424" lengthAdjust="spacingAndGlyphs">compartmentalization</text>
    <text class="attribute attribute--mid" x="1092" y="1313" textLength="339" lengthAdjust="spacingAndGlyphs">open mindedness</text>
    <text class="attribute attribute--light" x="1458" y="1313" textLength="166" lengthAdjust="spacingAndGlyphs">inclusive</text>
    <text class="attribute attribute--dark" x="1092" y="1375" textLength="154" lengthAdjust="spacingAndGlyphs">courage</text>
    <text class="attribute attribute--mid" x="1294" y="1375" textLength="181" lengthAdjust="spacingAndGlyphs">resilience</text>
    <text class="attribute attribute--light" x="1091" y="1435" textLength="193" lengthAdjust="spacingAndGlyphs">innovative</text>

    <!-- Vertical attributes -->
    <text class="attribute attribute--light" transform="translate(460 808) rotate(-90)" textLength="233" lengthAdjust="spacingAndGlyphs">selflessness</text>
    <text class="attribute attribute--light" transform="translate(510 808) rotate(-90)" textLength="358" lengthAdjust="spacingAndGlyphs">conscientiousness</text>
    <text class="attribute attribute--light" transform="translate(1106 878) rotate(-90)" textLength="268" lengthAdjust="spacingAndGlyphs">accountability</text>
    <text class="attribute attribute--light" transform="translate(1663 1182) rotate(-90)" textLength="245" lengthAdjust="spacingAndGlyphs">decisiveness</text>
    <text class="attribute attribute--light" transform="translate(1060 1440) rotate(-90)" textLength="150" lengthAdjust="spacingAndGlyphs">cunning</text>
  </g>
</svg>
</body>
</html>
```